Tralvo Miks flyer

I want this flyer to look like the one I upload here called tralvo miks. I want the to change to words (headline):"A new category in pet hydration" to: Ny unik produkt i Kategori hund. Also remove Functional elektrodryck för hundar.
Also change:" Vi tar emot Återförsäljarpartners" to "Kontakta oss för mer information"
If you think or see improvments plase do so. Its for a launch of a newe product to retailers (so not to the consumer).

Target Market(s)

Retail, stores, hotels, restaurants

Industry/Entity Type

Energy water for dogs

Colors
0054AA
0677BA
7BADD7
CADEEF
E8F1F8

Requirements
Must have
• Think zapfoxx, kordal bays, energy drinks but for dogs

```html
<!DOCTYPE html>
<html lang="sv">
<head>
<meta charset="utf-8">
<title>Tralvo Miks – återförsäljarflyer</title>
<link rel="stylesheet" href="https://fonts.googleapis.com/css2?family=Anton&family=Outfit:wght@300;400;500;600;700;800&display=swap">
<style>
  :root{
    --stage:#d4d4d4;
    --navy-deep:#0c1457;
    --navy:#13247a;
    --blue:#0054aa;
    --blue-bright:#0677ba;
    --sky:#0aa8e8;
    --sky-soft:#7badd7;
    --pale:#cadeef;
    --mist:#e8f1f8;
    --orange:#ff9a2e;
    --gold-a:#c99a2e;
    --gold-b:#f3d27a;
    --white:#ffffff;
    --text-soft:#dfe8f6;
  }
  *{box-sizing:border-box;margin:0;padding:0}
  html,body{width:1200px;height:1200px;overflow:hidden}
  body{background:var(--stage);font-family:"Outfit",sans-serif;color:var(--white);position:relative}

  .flyer{
    position:absolute;left:241px;top:92px;width:718px;height:1016px;overflow:hidden;
    background:
      radial-gradient(ellipse 380px 460px at 420px 430px,#1f6fd6 0%,#1548b0 40%,rgba(16,36,130,0) 75%),
      linear-gradient(180deg,#152a8c 0%,#112081 55%,var(--navy-deep) 100%);
    box-shadow:0 8px 24px rgba(0,0,0,.25);
  }
  .abs{position:absolute}

  /* header */
  .brand{left:40px;top:36px;display:flex;align-items:center;gap:8px}
  .brand-dot{width:30px;height:30px;border-radius:50%;background:var(--white)}
  .brand-name{font-weight:700;font-size:22px;line-height:20px;color:var(--white);width:80px}
  .brand-rule{left:195px;top:38px;width:1.5px;height:42px;background:var(--white)}
  .brand-tagline{left:214px;top:45px;font-weight:600;font-size:12.5px;line-height:14.5px;letter-spacing:.2px}

  .made-in{left:582px;top:0;width:106px;height:109px;background:var(--sky);border-radius:0 0 14px 14px;text-align:center;padding-top:34px}
  .made-in p{font-weight:700;font-size:13.5px;line-height:17px}
  .made-in svg{margin-top:6px}

  /* headline */
  .headline{left:34px;top:136px;font-family:"Anton",sans-serif;font-size:64px;line-height:62px;letter-spacing:-.5px;text-transform:uppercase}
  .headline .accent{color:var(--orange)}

  /* retailer reasons */
  .section-title{left:34px;top:428px;font-weight:600;font-size:17px;line-height:20.5px;letter-spacing:.3px}
  .rule-orange{height:1.5px;background:var(--orange)}
  .reasons{left:28px;top:523px;width:230px}
  .reason{position:absolute;left:0;width:240px}
  .icon-ring{position:absolute;left:0;top:0;width:36px;height:36px;border:1.2px solid var(--white);border-radius:50%;display:flex;align-items:center;justify-content:center}
  .reason h3{position:absolute;left:48px;top:5px;font-weight:700;font-size:10.6px;line-height:13px;color:var(--orange);width:200px}
  .reason p{position:absolute;left:49px;font-weight:300;font-size:10.6px;line-height:12.5px;color:var(--text-soft);width:160px}

  /* product */
  .product{left:279px;top:167px;width:176px;height:603px;border-radius:70px 70px 30px 30px;
    background:linear-gradient(180deg,#1a1a1a 0%,#1a1a1a 12%,#dfeaf6 16%,#f7fbff 30%,var(--blue) 53%,#2e3fa8 70%,#eef5fc 75%,#cfe0f2 100%)}

  /* benefits */
  .intro{left:486px;top:143px;font-weight:700;font-size:16px;line-height:20px;width:220px}
  .benefit{position:absolute;left:480px;width:230px}
  .benefit .icon-ring{width:47px;height:47px}
  .benefit h3{position:absolute;left:64px;top:3px;font-weight:700;font-size:12.3px;line-height:14.5px;color:var(--orange);width:150px}
  .benefit p{position:absolute;left:65px;font-weight:300;font-size:11px;line-height:15px;color:var(--text-soft);width:160px}
  .benefit-rule{position:absolute;left:545px;width:140px;height:1px;background:linear-gradient(90deg,rgba(255,255,255,0),rgba(255,255,255,.25),rgba(255,255,255,0))}

  .opportunity{left:527px;top:591px;width:161px;height:202px;border:1px solid rgba(201,154,46,.8);border-radius:10px;background:rgba(10,20,90,.35)}
  .opportunity h3{position:absolute;left:0;top:12px;width:100%;text-align:center;font-weight:700;font-size:12.3px;color:var(--sky)}
  .opportunity .divider{position:absolute;left:0;top:35px;width:100%;height:1px;background:rgba(201,154,46,.8)}
  .opportunity .copy{position:absolute;left:9px;top:47px;width:145px;font-weight:500;font-size:10.2px;line-height:13px}
  .opportunity svg{position:absolute;left:49px;top:97px}
  .opportunity .foot{position:absolute;left:0;top:160px;width:100%;text-align:center;font-weight:700;font-size:10.2px;line-height:13px}

  /* footer */
  .claim{left:36px;top:849px;font-weight:700;font-size:15.6px;letter-spacing:.25px;color:var(--orange);white-space:nowrap}
  .contact-cta{left:36px;top:889px;font-weight:700;font-size:27px;line-height:26px;color:var(--orange)}
  .contact-sub{left:34px;top:997px;font-weight:300;font-size:11.8px;color:var(--text-soft)}
  .v-rule{width:1px;background:var(--gold-a)}
  .contacts{left:311px;top:885px}
  .contact{display:flex;align-items:center;height:32px;font-weight:400;font-size:13px}
  .contact svg{width:16px;margin-right:20px}
  .launch-label{left:524px;top:887px;width:164px;text-align:center;font-weight:700;font-size:10.5px;letter-spacing:.1px;white-space:nowrap}
  .launch-date{left:523px;top:913px;width:165px;height:33px;background:linear-gradient(90deg,var(--gold-a),var(--gold-b) 45%,#e8b94f 70%,var(--gold-a));text-align:center;font-family:"Anton",sans-serif;font-size:22px;line-height:33px;color:#151515}
  .launch-note{left:536px;top:970px;font-weight:600;font-size:10.5px;line-height:13px}
</style>
</head>
<body>
<main class="flyer">

  <header>
    <div class="abs brand">
      <span class="brand-dot"></span>
      <span class="brand-name">tralvo miks</span>
    </div>
    <div class="abs brand-rule"></div>
    <p class="abs brand-tagline">FUNCTIONAL HYDRATION<br>FÖR HUNDAR</p>

    <div class="abs made-in">
      <p>TILLVERKAD I<br>SVERIGE</p>
      <svg width="38" height="24" viewBox="0 0 38 24" aria-label="Sveriges flagga">
        <rect width="38" height="24" fill="#005cbf"/>
        <rect x="11" width="6" height="24" fill="#fecc00"/>
        <rect y="9" width="38" height="6" fill="#fecc00"/>
      </svg>
    </div>
  </header>

  <h1 class="abs headline">Ny unik<br>produkt i<br><span class="accent">kategori<br>hund</span></h1>

  <h2 class="abs section-title">VARFÖR<br>ÅTERFÖRSÄLJARE<br>VÄLJER TRALVO MIKS</h2>
  <div class="abs rule-orange" style="left:34px;top:499px;width:53px"></div>

  <section class="abs reasons">
    <div class="reason" style="top:0">
      <span class="icon-ring"><svg width="18" height="18" viewBox="0 0 18 18" fill="none" stroke="#fff" stroke-width="1.3"><path d="M2 16h14"/><path d="M3 12l4-4 3 3 5-6"/><path d="M12 5h3v3"/></svg></span>
      <h3>HÖG MARGINAL,<br>LITEN KONKURRENS</h3>
      <p style="top:40px">Var först på en växande kategori.</p>
    </div>
    <div class="reason" style="top:70px">
      <span class="icon-ring"><svg width="18" height="18" viewBox="0 0 18 18" fill="none" stroke="#fff" stroke-width="1.3"><path d="M1 2h3l2 9h9l2-6H5"/><circle cx="7" cy="15" r="1.3"/><circle cx="14" cy="15" r="1.3"/></svg></span>
      <h3>SNABBT VÄXANDE SEGMENT<br>INOM HUNDHÄLSA</h3>
      <p style="top:40px">Stark och ökande efterfrågan från medvetna hundägare.</p>
    </div>
    <div class="reason" style="top:141px">
      <span class="icon-ring"><svg width="18" height="18" viewBox="0 0 18 18" fill="none" stroke="#fff" stroke-width="1.3"><path d="M9 16S2 11 2 6.5A3.5 3.5 0 0 1 9 5a3.5 3.5 0 0 1 7 1.5C16 11 9 16 9 16z"/></svg></span>
      <h3>STOR<br>IMPULSKÖPSPOTENTIAL</h3>
      <p style="top:40px">Perfekt att placera vid vatten och snacks.</p>
    </div>
    <div class="reason" style="top:208px">
      <span class="icon-ring"><svg width="18" height="18" viewBox="0 0 18 18" fill="none" stroke="#fff" stroke-width="1.3"><path d="M10 2h6v6l-8 8-6-6z"/><circle cx="13" cy="5" r="1"/></svg></span>
      <h3>PREMIUMPOSITIONERING<br>= HÖGRE KUNDVÄRDE</h3>
      <p style="top:40px">Ger mer värde i varje besök.</p>
    </div>
  </section>

  <div class="abs product" role="img" aria-label="Produktbild: genomskinlig 500 ml-flaska elektrolytdryck för hundar med svart kork och blå etikett, vattenstänk runt botten"></div>

  <p class="abs intro">Utvecklad för alla hundar. Inspirerad av human sportdryck.</p>
  <div class="abs rule-orange" style="left:486px;top:209px;width:48px"></div>

  <section>
    <div class="benefit" style="top:233px">
      <span class="icon-ring"><svg width="22" height="22" viewBox="0 0 22 22" fill="none" stroke="#fff" stroke-width="1.3"><path d="M11 2C8 7 5 10 5 14a6 6 0 0 0 12 0c0-4-3-7-6-12z"/><path d="M9 16c0-2 1.5-3.5 4-4"/></svg></span>
      <h3>NATURLIGA<br>ELEKTROLYTER</h3>
      <p style="top:37px">Återställer vätska och stödjer balansen.</p>
    </div>
    <div class="benefit-rule" style="top:313px"></div>
    <div class="benefit" style="top:328px">
      <span class="icon-ring"><svg width="22" height="22" viewBox="0 0 22 22" fill="none" stroke="#fff" stroke-width="1.3"><path d="M11 2C9 6 7 8 7 11a4 4 0 0 0 8 0c0-3-2-5-4-9z"/><ellipse cx="11" cy="18" rx="8" ry="2.2"/></svg></span>
      <h3>STÖDJER HYDRERING<br>&amp; ÅTERHÄMTNING</h3>
      <p style="top:37px">Hjälper till att upprätthålla prestationsförmåga och välmående.</p>
    </div>
    <div class="benefit-rule" style="top:422px"></div>
    <div class="benefit" style="top:438px">
      <span class="icon-ring"><svg width="22" height="22" viewBox="0 0 22 22" fill="none" stroke="#fff" stroke-width="1.3"><path d="M3 15l4-4 3 3 8-8"/><path d="M14 6h4v4"/></svg></span>
      <h3>PERFEKT EFTER<br>AKTIVITET, VÄRME &amp;<br>RESA</h3>
      <p style="top:51px">För vardagens äventyr och särskilda tillfällen.</p>
    </div>
  </section>

  <aside class="abs opportunity">
    <h3>KATEGORIMÖJLIGHET</h3>
    <div class="divider"></div>
    <p class="copy">Hundhydrering för hundar är ett outnyttjat segment med stor tillväxtpotential.</p>
    <svg width="54" height="50" viewBox="0 0 54 50" aria-label="Stigande stapeldiagram">
      <g fill="var(--orange)">
        <rect x="2" y="40" width="8" height="8"/>
        <rect x="15" y="34" width="8" height="14"/>
        <rect x="28" y="27" width="8" height="21"/>
        <rect x="41" y="16" width="8" height="32"/>
        <path d="M0 32C14 30 30 22 42 8l-4-2 12-4-2 12-3-3C34 26 16 34 1 36z"/>
      </g>
    </svg>
    <p class="foot">VÄXANDE EFTERFRÅGAN<br>I HELA EUROPA</p>
  </aside>

  <footer>
    <p class="abs claim">RENA INGREDIENSER. VERKLIGA FÖRDELAR. HUNDAR KÄNNER SKILLNADEN.</p>

    <h2 class="abs contact-cta">Kontakta oss för<br>mer information</h2>
    <p class="abs contact-sub">Bli en del av framtidens hundhydrering.</p>

    <div class="abs v-rule" style="left:293px;top:881px;height:97px"></div>

    <div class="abs contacts">
      <div class="contact"><svg viewBox="0 0 16 16" height="16" fill="var(--gold-a)"><path d="M4 1l2.5 3.5-1.5 2c1 2 2.5 3.5 4.5 4.5l2-1.5L15 12l-2 3C7 15 1 9 1 3z"/></svg>+46 70 123 45 67</div>
      <div class="contact"><svg viewBox="0 0 16 16" height="16" fill="none" stroke="var(--gold-a)" stroke-width="1.3"><rect x="1" y="3.5" width="14" height="9"/><path d="M1 3.5l7 5 7-5"/></svg>info@tralvomiks.com</div>
      <div class="contact"><svg viewBox="0 0 16 16" height="16" fill="none" stroke="var(--gold-a)" stroke-width="1.2"><circle cx="8" cy="8" r="7"/><ellipse cx="8" cy="8" rx="3" ry="7"/><path d="M1 8h14M2.5 4.5h11M2.5 11.5h11"/></svg>tralvomiks.com</div>
    </div>

    <div class="abs v-rule" style="left:499px;top:881px;height:97px"></div>

    <p class="abs launch-label">— BEGRÄNSAD LANSERING —</p>
    <div class="abs launch-date">SOMMAREN 2026</div>
    <p class="abs launch-note">Säkra din tilldelning<br>i tid och möt efterfrågan.</p>
  </footer>

</main>
</body>
</html>
```